biz card for insurance Agent
Insurance Agency Biz card
biz card for insurance Agent - Health
Creative Brief
Professional
Marla Tovesby
Insurance Agent
NC & SC
marlatovesby@quillmail.example
please create a design for the back of the card, and we'll add the text to it later

```html
<!DOCTYPE html>
<html lang="en">
<head>
<meta charset="utf-8">
<title>Piedmont Shield Partners – Business Card</title>
<link href="https://fonts.googleapis.com/css2?family=Oswald:wght@600&family=Roboto:wght@400;700&display=swap" rel="stylesheet">
<style>
  :root {
    --bg: #5a5a5a;
    --bg-light: #777;
    --red: #c8202a;
    --red-dark: #8e141b;
    --blue: #3f7fa8;
    --blue-light: #6aa6cc;
    --navy: #1d3346;
    --ink: #1b1b1b;
    --white: #ffffff;
    --map-white: #f4f4f4;
  }
  * { box-sizing: border-box; margin: 0; padding: 0; }
  html, body { width: 1200px; height: 607px; overflow: hidden; }
  body {
    background: radial-gradient(ellipse at 50% 40%, var(--bg-light), var(--bg) 75%);
    font-family: "Roboto", Arial, sans-serif;
    position: relative;
  }
  .card {
    position: absolute;
    top: 156px;
    width: 520px;
    height: 296px;
    overflow: hidden;
    box-shadow: 0 12px 28px rgba(0,0,0,.45);
  }
  .card--front { left: 50px; background: var(--white); }
  .card--back { left: 630px; background: linear-gradient(160deg, var(--blue-light), var(--blue) 55%, #2f6a92); }

  /* front */
  .top-strip { position: absolute; left: 0; top: 0; width: 100%; height: 10px; background: var(--ink); }
  .top-strip span { position: absolute; top: 0; height: 10px; background: var(--red); }
  .logo-area { position: absolute; left: 0; top: 10px; width: 320px; height: 160px; display: flex; align-items: center; justify-content: center; gap: 10px; }
  .brand-mark { width: 22px; height: 22px; background: var(--red); flex: none; }
  .brand-name { font-family: "Oswald", Arial, sans-serif; font-weight: 600; color: var(--red); font-size: 25px; line-height: 1.05; letter-spacing: 1px; text-transform: uppercase; }
  .agent-panel { position: absolute; left: 320px; top: 10px; width: 200px; height: 140px; background: linear-gradient(180deg, var(--blue-light), var(--blue)); padding: 18px 0 0 70px; color: var(--white); }
  .agent-name { font-size: 15px; font-weight: 400; }
  .agent-title { font-size: 11px; margin-top: 3px; }
  .agent-photo { position: absolute; left: 14px; top: 50px; width: 50px; height: 66px; background: linear-gradient(180deg, #d9d9d9, #8b8b8b); border: 2px solid var(--white); }
  .contact-email { position: absolute; left: 0; top: 170px; width: 150px; height: 126px; background: linear-gradient(180deg, var(--red), var(--red-dark)); color: var(--white); padding: 22px 10px; font-size: 10px; line-height: 1.5; }
  .contact-email strong { display: block; font-size: 12px; }
  .contact-region { position: absolute; left: 150px; top: 170px; width: 110px; height: 126px; background: var(--navy); color: var(--white); padding: 22px 10px; font-size: 11px; line-height: 1.6; }
  .contact-region .region { font-weight: 700; font-size: 12px; }
  .map-panel { position: absolute; left: 260px; top: 150px; width: 260px; height: 146px; background: linear-gradient(160deg, var(--red), var(--red-dark)); }
  .map-area { position: absolute; left: 40px; top: 22px; width: 180px; height: 100px; background: linear-gradient(135deg, var(--map-white) 55%, var(--ink) 56%); opacity: .95; }

  /* back */
  .back-logo { position: absolute; left: 0; top: 0; width: 100%; height: 240px; display: flex; align-items: center; justify-content: center; gap: 12px; }
  .back-logo .brand-name { color: var(--navy); font-size: 30px; }
  .back-logo .brand-mark { background: var(--navy); width: 26px; height: 26px; }
  .bottom-stripes { position: absolute; left: 0; bottom: 0; width: 100%; height: 44px; }
  .bottom-stripes .band { position: absolute; left: 0; width: 100%; }
  .band--light { top: 0; height: 10px; background: #cfe3ef; }
  .band--red { top: 10px; height: 18px; background: var(--red); }
  .band--dark { top: 28px; height: 16px; background: var(--ink); }
  .band--dark span { position: absolute; top: 0; height: 16px; width: 40px; background: var(--red-dark); }
</style>
</head>
<body>
  <section class="card card--front" aria-label="Business card front">
    <div class="top-strip"><span style="left:60px;width:50px"></span><span style="left:240px;width:70px"></span><span style="left:420px;width:50px"></span></div>
    <div class="logo-area">
      <div class="brand-mark"></div>
      <div class="brand-name">Piedmont Shield<br>Partners</div>
    </div>
    <div class="agent-panel">
      <div class="agent-photo" role="img" aria-label="Portrait photo of the agent"></div>
      <p class="agent-name">Marla Tovesby</p>
      <p class="agent-title">Insurance Agent</p>
    </div>
    <div class="contact-email">
      <strong>Email:</strong>
      marlatovesby@<br>quillmail.example
    </div>
    <div class="contact-region">
      <p class="region">NC &amp; SC</p>
      <p>Tell: 555.013.2790</p>
    </div>
    <div class="map-panel">
      <div class="map-area" role="img" aria-label="Map of North Carolina and South Carolina"></div>
    </div>
  </section>

  <section class="card card--back" aria-label="Business card back">
    <div class="back-logo">
      <div class="brand-mark"></div>
      <div class="brand-name">Piedmont Shield<br>Partners</div>
    </div>
    <div class="bottom-stripes">
      <div class="band band--light"></div>
      <div class="band band--red"></div>
      <div class="band band--dark"><span style="left:90px"></span><span style="left:250px"></span><span style="left:410px"></span></div>
    </div>
  </section>
</body>
</html>
```